Exhibition stand design counter and wall

We need a design for our exhibition stand.
We are a sheet metal processing company (laser cutting, welding, sheet metal bending,...)

The stand should be a universal stand that can be used for both technical trade fairs and human resources trade fairs.
Our website www.kaltenmoor-vrt.de has been redesigned.
It would be nice if the design could be based on this. I can provide all images on the website in high resolution - please enquire here.
The appendix contains data sheets on the required print format.

Please refer to the logo for the color definition of our company colors.

```html
<!DOCTYPE html>
<html lang="en">
<head>
<meta charset="utf-8">
<title>Kaltenmoor Blechtechnik – Exhibition Stand</title>
<link rel="stylesheet" href="https://fonts.googleapis.com/css2?family=Rubik:ital,wght@0,600;1,800&display=swap">
<style>
  :root {
    --navy: #223d7a;
    --navy-deep: #1a3066;
    --teal: #3e7b8a;
    --steel-dark: #1f2c3a;
    --steel-mid: #4f7ea3;
    --steel-light: #9fcbe6;
    --mint: #7fdcc0;
    --glow: #a8f7e6;
    --frame: #b3b7bc;
    --white: #ffffff;
    --orange: #f1a64f;
    --black: #0b0b0e;
    --stage-a: #1d3f8f;
    --stage-b: #a9bde5;
  }
  * { margin: 0; padding: 0; box-sizing: border-box; }
  html, body { width: 1200px; height: 896px; overflow: hidden; }
  body {
    background: linear-gradient(120deg, var(--stage-a) 0%, #5470b0 40%, var(--stage-b) 100%);
    position: relative;
    font-family: "Rubik", sans-serif;
  }
  .defs { position: absolute; width: 0; height: 0; }
  .panel { position: absolute; display: block; box-shadow: 0 2px 6px rgba(0,0,0,.25); }
  .wall-main { left: 70px; top: 34px; width: 600px; height: 394px; }
  .counter-flat { left: 725px; top: 248px; width: 381px; height: 180px; }
  .wall-preview { left: 300px; top: 480px; width: 600px; height: 394px; }
  .counter-front { left: 370px; top: 675px; width: 150px; height: 198px; box-shadow: 0 3px 8px rgba(0,0,0,.4); }
  .brand-name { font-family: "Rubik", sans-serif; font-weight: 600; fill: var(--navy); }
  .tagline { font-family: "Rubik", sans-serif; font-weight: 800; font-style: italic; fill: var(--glow); filter: url(#text-glow); }
</style>
</head>
<body>

<svg class="defs" aria-hidden="true">
  <defs>
    <linearGradient id="swoosh-fill" x1="0" y1="1" x2="1" y2="0">
      <stop offset="0" stop-color="var(--mint)"/>
      <stop offset=".3" stop-color="#6fa6c8"/>
      <stop offset=".6" stop-color="var(--steel-mid)"/>
      <stop offset=".85" stop-color="#2c3e52"/>
      <stop offset="1" stop-color="var(--steel-dark)"/>
    </linearGradient>
    <linearGradient id="counter-fill" x1="0" y1="1" x2="1" y2="0">
      <stop offset="0" stop-color="#4d7ea6"/>
      <stop offset=".45" stop-color="var(--steel-light)"/>
      <stop offset="1" stop-color="#3c6688"/>
    </linearGradient>
    <radialGradient id="laser-photo" cx=".5" cy=".45" r=".6">
      <stop offset="0" stop-color="#d9dde2"/>
      <stop offset=".55" stop-color="#8c96a2"/>
      <stop offset="1" stop-color="#2b3a4e"/>
    </radialGradient>
    <linearGradient id="part-photo" x1="0" y1="0" x2="1" y2="1">
      <stop offset="0" stop-color="#eef1f4"/>
      <stop offset=".6" stop-color="#b9c2cc"/>
      <stop offset="1" stop-color="#dfe4ea"/>
    </linearGradient>
    <filter id="text-glow" x="-20%" y="-50%" width="140%" height="200%">
      <feDropShadow dx="0" dy="1" stdDeviation="1.2" flood-color="#0b1d33" flood-opacity=".9"/>
    </filter>
    <filter id="photo-glow" x="-30%" y="-30%" width="160%" height="160%">
      <feDropShadow dx="0" dy="0" stdDeviation="4" flood-color="#b8f4ff" flood-opacity=".9"/>
    </filter>

    <symbol id="wall-graphic" viewBox="0 0 600 394">
      <rect width="600" height="394" fill="var(--navy)"/>
      <path d="M0,336 C160,318 300,350 430,352 C520,354 585,300 600,250 V300 C580,360 520,394 430,390 C300,386 160,360 0,370 Z" fill="var(--teal)"/>
      <path d="M600,0 C470,8 380,80 320,160 C270,230 200,280 0,288 V345 C150,322 300,358 430,360 C525,362 590,290 600,215 Z" fill="url(#swoosh-fill)"/>
      <path d="M0,0 H600 C470,5 390,70 330,140 C290,200 230,270 120,282 C70,287 30,286 0,287 Z" fill="var(--white)"/>
      <path d="M0,158 H258 C235,195 200,235 140,252 C90,264 40,262 0,264 Z" fill="var(--navy)" stroke="var(--teal)" stroke-width="2"/>

      <circle cx="112" cy="79" r="24" fill="none" stroke="var(--navy)" stroke-width="4"/>
      <text class="brand-name" x="145" y="104" font-size="22">KALTENMOOR<tspan x="168" y="126" font-size="12.5" letter-spacing="1">BLECHTECHNIK</tspan></text>

      <text class="tagline" x="436" y="76" font-size="13" text-anchor="middle">Precision in<tspan x="436" y="89">every beam</tspan></text>

      <g filter="url(#photo-glow)">
        <rect x="275" y="193" width="144" height="81" rx="7" fill="var(--frame)"/>
      </g>
      <rect x="281" y="199" width="132" height="69" rx="3" fill="url(#part-photo)" role="img" aria-label="Photo of a laser-cut sheet metal part"/>
      <g filter="url(#photo-glow)">
        <circle cx="442" cy="175" r="56" fill="var(--frame)"/>
      </g>
      <circle cx="442" cy="175" r="51" fill="url(#laser-photo)" role="img" aria-label="Photo of a laser cutting head over a metal sheet"/>

      <text class="tagline" x="355" y="304" font-size="13" text-anchor="middle">Precision that shapes the future:<tspan x="355" y="317">your metal, our expertise</tspan></text>
    </symbol>

    <symbol id="counter-graphic" viewBox="0 0 381 180">
      <rect width="381" height="180" fill="var(--navy)"/>
      <path d="M0,70 C40,160 90,200 160,175 C240,145 330,60 381,90 V110 C330,80 240,160 160,190 L0,190 Z" fill="var(--teal)"/>
      <ellipse cx="195" cy="90" rx="150" ry="62" transform="rotate(-22 195 90)" fill="url(#counter-fill)"/>
      <path d="M0,80 C40,170 90,190 160,172 C250,148 320,70 381,40" fill="none" stroke="var(--frame)" stroke-width="5"/>
      <path d="M60,150 C120,40 260,0 330,20 C360,30 375,60 381,100" fill="none" stroke="var(--frame)" stroke-width="5"/>
      <circle cx="190" cy="86" r="11" fill="none" stroke="var(--navy)" stroke-width="2.5"/>
      <text class="brand-name" x="190" y="115" font-size="11.5" text-anchor="middle">KALTENMOOR<tspan x="190" y="124" font-size="6.5" letter-spacing=".6">BLECHTECHNIK</tspan></text>
    </symbol>
  </defs>
</svg>

<svg class="panel wall-main" viewBox="0 0 600 394" role="group" aria-label="Exhibition wall">
  <use href="#wall-graphic"/>
</svg>

<svg class="panel counter-flat" viewBox="0 0 381 180" role="group" aria-label="Exhibition counter">
  <use href="#counter-graphic"/>
</svg>

<svg class="panel wall-preview" viewBox="0 0 600 394" role="group" aria-label="Exhibition wall with counter">
  <use href="#wall-graphic"/>
</svg>

<svg class="panel counter-front" viewBox="0 0 150 198" role="group" aria-label="Counter front">
  <rect width="150" height="198" fill="var(--navy)"/>
  <rect width="150" height="4" fill="var(--orange)"/>
  <rect y="4" width="150" height="6" fill="var(--black)"/>
  <ellipse cx="75" cy="105" rx="110" ry="58" transform="rotate(-18 75 105)" fill="url(#counter-fill)"/>
  <path d="M0,62 C50,30 110,20 150,32" fill="none" stroke="var(--frame)" stroke-width="4"/>
  <path d="M0,172 C50,162 110,140 150,120" fill="none" stroke="var(--frame)" stroke-width="4"/>
  <circle cx="74" cy="96" r="11" fill="none" stroke="var(--navy)" stroke-width="2.5"/>
  <text class="brand-name" x="74" y="125" font-size="11" text-anchor="middle">KALTENMOOR<tspan x="74" y="134" font-size="6.3" letter-spacing=".5">BLECHTECHNIK</tspan></text>
  <rect y="191" width="150" height="7" fill="var(--black)"/>
</svg>

</body>
</html>
```